"HTML Email Template"

We are wanting to get a html template built for the purpose of a monthly email that we send out to our database. Currently we send them out in an email form and looking to bring some more colour and graphics to jazz it up a little.
Our webpage address is www.harborlineadvisory.com.au
It targets people in the innovation, development, strategy, collaboration and entrepreneurship space.
The monthly email contains an into paragraph and up to about ten items with links to articles etc
We would like to stick with a similar colour scheme as seen on our webpage.
The final design should look professional and edgy
Updates

Hi

We have just changed this status of this project to Guaranteed Payment
Looking forward to start receiving some great designs
Thanks

Project Deadline Extended

Target Market(s)

Senior executives in corporations, professionals

Industry/Entity Type

It Professional

```html
<!DOCTYPE html>
<html lang="en">
<head>
<meta charset="utf-8">
<title>Harborline Advisory – Monthly Email</title>
<link href="https://fonts.googleapis.com/css2?family=Arimo:wght@400;700&family=Dancing+Script:wght@600&display=swap" rel="stylesheet">
<style>
:root{
  --page:#eeeef5;
  --navy:#3b4d68;
  --navy-dark:#34445c;
  --slate:#8797a6;
  --rule:#d9dde3;
  --ink:#1b1b1b;
  --muted:#8a8a8a;
  --white:#ffffff;
  --panel:#2b6f8a;
  --panel-dark:#0e232c;
  --cyan:#3fd0ee;
  --pill:#173340;
}
*{box-sizing:border-box;margin:0;padding:0}
html,body{width:1200px;height:900px;overflow:hidden}
body{background:var(--page);font-family:"Arimo",Arial,sans-serif;color:var(--ink);position:relative}
.abs{position:absolute}
.preheader{left:0;width:1243px;top:14px;text-align:center;font-size:6px;color:#333}
.preheader a{color:#333}
.topbar{left:449px;top:39px;width:331px;height:21px;background:var(--navy);color:#fff;font-size:6.5px;line-height:21px;padding-left:20px}
.topbar em{font-style:italic;margin-right:4px}
.topbar b{font-weight:700}
.topstrip{left:449px;top:60px;width:331px;height:6px;background:#b4c0cc}
.mail{left:463px;top:66px;width:317px;height:792px;background:var(--white);box-shadow:0 0 4px rgba(0,0,0,.15)}
.brand{left:10px;top:14px;display:flex;align-items:center;gap:6px}
.brand-mark{width:24px;height:24px;border-radius:50%;background:var(--navy)}
.brand-name{font-size:15px;font-weight:700;color:var(--navy);letter-spacing:-.3px}
.social{right:18px;top:18px;display:flex;gap:4px}
.social span{width:17px;height:17px;border-radius:50%;background:#4f7fb8}
.social span:last-child{background:#79b5df}
.head-rule{left:8px;right:8px;top:51px;height:1px;background:var(--rule)}
.hero{left:0;top:60px;width:317px;height:110px;background:linear-gradient(#3e506b,#46586f);color:#fff;padding:6px 10px}
.hero h1{font-weight:400;font-size:20px;margin-bottom:6px}
.hero p{font-size:6.2px;line-height:1.3;margin-bottom:7px}
.hero a{color:#fff}
.hero .sign{color:#cfe0ee}
.band{left:0;top:170px;width:317px;height:24px;background:var(--slate);color:#fff;font-size:7px;font-weight:700;text-align:center;line-height:24px}
.article{left:10px;width:297px;height:135px;border:1px solid var(--rule);background:#fff}
.art-img{left:8px;top:8px;width:124px;height:116px;background:linear-gradient(#f4f4f4,#dcdcdc)}
.art-body{left:140px;top:16px;width:150px}
.art-body h2{font-weight:400;font-size:8.6px;line-height:1.35;color:#111;margin-bottom:7px}
.art-body p{font-size:5.7px;line-height:1.4;color:var(--muted)}
.more{right:8px;font-size:5px;color:#222}
.shares{left:140px;display:flex;gap:6px}
.shares span{font-size:5px;border:1px solid #c8ccd4;background:#f3f5f8;padding:2px 4px;color:#333;display:flex;align-items:center;gap:2px}
.shares i{display:inline-block;width:5px;height:5px;background:#5f86bd}
.load-rule{left:6px;right:6px;top:680px;height:1px;background:var(--rule)}
.load-btn{left:147px;top:668px;width:24px;height:24px;border-radius:50%;background:#e2e4e8;border:2px solid #fff}
.load-txt{left:0;width:317px;top:697px;text-align:center;font-size:4.5px;font-weight:700}
.foot1{left:0;top:734px;width:317px;height:26px;background:linear-gradient(#5a6f90,#4a5d79);color:#fff;font-size:5px;text-align:center;line-height:20px}
.foot-nav{left:0;top:760px;width:317px;height:9px;background:#b0b4ba;display:flex;justify-content:center;gap:12px;font-size:4.6px;color:#fff;line-height:9px}
.foot2{left:0;top:769px;width:317px;height:23px;background:var(--navy-dark);color:#fff;font-size:5px;text-align:center;line-height:32px}
.legal{left:449px;width:331px;top:865px;text-align:center;font-size:5.5px;line-height:1.3;color:#222}
.legal a{color:#1f4f8a;text-decoration:none}
.panel{left:1016px;top:166px;width:184px;height:506px;background:var(--panel);border-radius:6px 0 0 6px;overflow:hidden}
.panel-title{top:27px;left:0;width:184px;text-align:center;color:#fff;font-size:11px;line-height:1.2}
.clients{top:64px;left:0;width:184px;height:242px;background:var(--panel-dark)}
.clients span{position:absolute;width:40px;height:40px;border-radius:8px}
.among{top:212px;left:0;width:184px;text-align:center;color:var(--cyan);font-size:11px}
.pill{left:8px;width:170px;height:17px;background:var(--pill);border-radius:4px;color:#fff;font-size:11px;line-height:17px;padding-left:50px}
.pill svg{position:absolute;left:17px;top:5px}
.love{top:470px;left:0;width:184px;text-align:center;font-family:"Dancing Script",cursive;color:#111;font-size:14px}
</style>
</head>
<body>
<div class="abs preheader">Having trouble viewing this mail? <a href="#">View it in your browser.</a></div>
<div class="abs topbar"><em>Harborline Advisory</em> <b>January 2012</b></div>
<div class="abs topstrip"></div>

<main class="abs mail">
  <div class="abs brand"><span class="brand-mark"></span><span class="brand-name">Harborline Advisory</span></div>
  <div class="abs social"><span></span><span></span><span></span></div>
  <div class="abs head-rule"></div>

  <section class="abs hero">
    <h1>Hey Friend!</h1>
    <p>We have pretty cool news this week for you. We went to California and got an interview with <a href="#">Martin Ellery</a>, oh. woow. He's sharing very cool ideas of how Linkwave is doing to engage its users and how they became the top social network site with more than 600M active users every month.</p>
    <p>Also we keep sharing innovation ideas and awesome articles. Enjoy.</p>
    <p class="sign">- Harborline Advisory</p>
  </section>
  <div class="abs band">HERE ARE SOME COOL ARTICLES YOU CAN'T LOSE THIS WEEK</div>

  <article class="abs article" style="top:222px">
    <div class="abs art-img" role="img" aria-label="Sketch of three people sharing ideas with the word Collaboration"></div>
    <div class="abs art-body"><h2>Open Innovation – What's Behind the Buzzword? – Kestrel and Northbeam</h2><p>Innovation is higher than ever on companies' agenda. 62% of executives interviewed in a recent survey say their business strategy is "largely" or "totally" dependent on innovation...</p></div>
    <div class="abs more" style="top:92px">&gt; Read more</div>
    <div class="abs shares" style="top:112px"><span><i></i>Like</span><span><i></i>Post</span><span><i></i>Share</span></div>
  </article>

  <article class="abs article" style="top:373px">
    <div class="abs art-img" role="img" aria-label="Sketch of a coffee cup spilling with the words Wake up your thinking"></div>
    <div class="abs art-body"><h2>Transformative Times: New Opportunities for Business in an Era of Upheaval</h2><p>In this report from the Calder Institute of Management &amp; International Studies, students explore the ways that the business community has responded to changes in our global economy...</p></div>
    <div class="abs more" style="top:92px">&gt; Read more</div>
    <div class="abs shares" style="top:112px"><span><i></i>Like</span><span><i></i>Post</span><span><i></i>Share</span></div>
  </article>

  <article class="abs article" style="top:524px">
    <div class="abs art-img" role="img" aria-label="Sketch of three people sharing ideas with the word Collaboration"></div>
    <div class="abs art-body"><h2>Open Innovation – What's Behind the Buzzword? – Kestrel and Northbeam</h2><p>Innovation is higher than ever on companies' agenda. 62% of executives interviewed in a recent survey say their business strategy is "largely" or "totally" dependent on innovation...</p></div>
    <div class="abs more" style="top:92px">&gt; Read more</div>
    <div class="abs shares" style="top:112px"><span><i></i>Like</span><span><i></i>Post</span><span><i></i>Share</span></div>
  </article>

  <div class="abs load-rule"></div>
  <div class="abs load-btn">
    <svg width="20" height="20" viewBox="0 0 20 20"><path d="M6 5l4 4 4-4M6 10l4 4 4-4" fill="none" stroke="#8a96a6" stroke-width="1.6"/></svg>
  </div>
  <div class="abs load-txt">LOAD MORE ARTICLES</div>

  <div class="abs foot1">Harborline Advisory · Keeping you at the leading edge!</div>
  <nav class="abs foot-nav"><span>Innovation</span>|<span>Collaboration</span>|<span>Globalization</span>|<span>Entrepreneurship</span>|<span>Crowdsourcing</span>|<span>Ideation</span></nav>
  <div class="abs foot2">About Us &nbsp; Contact Us</div>
</main>

<div class="abs legal">Copyright © 2012 Harborline Advisory Pty Ltd. All Rights Reserved.<br>14 Ferris Lane Harbord NSW 2096 Australia<br>- <a href="#">www.harborlineadvisory.com.au</a> -</div>

<aside class="abs panel">
  <div class="abs panel-title">Tested in all major<br>email clients</div>
  <div class="abs clients">
    <span style="left:16px;top:16px;background:#7b3a9e;border-radius:50%"></span>
    <span style="left:80px;top:16px;background:#c9302c"></span>
    <span style="left:134px;top:12px;background:#3f79b8;border-radius:4px;width:34px;height:34px"></span>
    <span style="left:22px;top:74px;background:#9cc43a;border-radius:50%"></span>
    <span style="left:80px;top:82px;background:#2f5e9e;border-radius:50%;width:46px;height:46px"></span>
    <span style="left:136px;top:82px;background:#c9a046"></span>
    <span style="left:52px;top:146px;background:#f2b51a;border-radius:50%"></span>
    <span style="left:112px;top:146px;background:#7f9bb8;width:36px;height:40px"></span>
    <div class="abs among">among others</div>
  </div>
  <div class="abs pill" style="top:389px"><svg width="14" height="7" viewBox="0 0 14 7"><path d="M0 3.5h12M9 1l3 2.5L9 6" fill="none" stroke="#3fd0ee" stroke-width="1"/></svg>Handmade code</div>
  <div class="abs pill" style="top:417px"><svg width="14" height="7" viewBox="0 0 14 7"><path d="M0 3.5h12M9 1l3 2.5L9 6" fill="none" stroke="#3fd0ee" stroke-width="1"/></svg>Include SPAM test</div>
  <div class="abs love">Made with Love</div>
</aside>
</body>
</html>
```